5 year service award card*

I'm attaching a celebration type card in which I need a new card similar made but with KVR logo's on it instead.

Colors

Designer to choose colors to be used in the design.

```html
<!DOCTYPE html>
<html lang="en">
<head>
<meta charset="utf-8">
<title>5 Year Anniversary Service Award</title>
<link rel="stylesheet" href="https://fonts.googleapis.com/css2?family=Poiret+One&family=Quicksand:wght@300;400;500&display=swap">
<style>
  :root {
    --page: #ffffff;
    --card: #191e2a;
    --gold: #c9a041;
    --gold-light: #f0d27a;
    --gold-dark: #8f6a1e;
    --ink: #eceef2;
    --sign: #2b303c;
  }
  * { margin: 0; padding: 0; box-sizing: border-box; }
  html, body {
    width: 927px; height: 1200px; overflow: hidden;
    background: var(--page);
  }
  .award-card {
    position: absolute; left: 142px; top: 90px;
    width: 685px; height: 1005px;
    background: var(--card);
    color: var(--ink);
    font-family: "Quicksand", sans-serif;
  }
  .frame-line { position: absolute; background: var(--gold); }
  .frame-line.horizontal { left: 138px; width: 422px; height: 1px; }
  .frame-line.vertical { top: 92px; height: 806px; width: 1px; }
  .frame-line.top-a { top: 44px; }
  .frame-line.top-b { top: 51px; }
  .frame-line.bottom-a { top: 966px; }
  .frame-line.bottom-b { top: 973px; }
  .frame-line.left-a { left: 40px; }
  .frame-line.left-b { left: 50px; }
  .frame-line.right-a { right: 40px; }
  .frame-line.right-b { right: 50px; }

  .corner-ornament {
    position: absolute; width: 96px; height: 90px;
    background: radial-gradient(circle at 40% 40%, var(--gold-light), var(--gold) 50%, var(--gold-dark));
    opacity: 0.85;
  }
  .corner-ornament.top-left { left: 36px; top: 30px; }
  .corner-ornament.top-right { right: 36px; top: 30px; }
  .corner-ornament.bottom-left { left: 36px; bottom: 30px; }
  .corner-ornament.bottom-right { right: 36px; bottom: 30px; }

  .heading-arc {
    position: absolute; left: 0; top: 100px;
    width: 685px; height: 100px;
  }
  .heading-arc text {
    font-family: "Poiret One", sans-serif;
    font-size: 50px; letter-spacing: 1px;
    fill: var(--gold);
  }
  .years-number, .years-label {
    position: absolute; left: 0; width: 100%;
    text-align: center;
    font-family: "Poiret One", sans-serif;
    color: var(--gold);
  }
  .years-number { top: 186px; font-size: 72px; line-height: 72px; }
  .years-label { top: 242px; font-size: 68px; line-height: 68px; letter-spacing: 5px; }

  .thanks-message {
    position: absolute; left: 60px; top: 340px; width: 565px;
    text-align: center;
    font-size: 25px; line-height: 36px; font-weight: 400;
  }
  .gold-rule {
    position: absolute; left: 162px; width: 363px; height: 3px;
    background: linear-gradient(90deg, var(--gold-dark), var(--gold-light), var(--gold));
  }
  .gold-rule.above-date { top: 564px; }
  .gold-rule.below-date { top: 669px; }

  .award-date { position: absolute; top: 574px; left: 0; width: 100%; height: 92px; }
  .award-date span { position: absolute; top: 0; height: 92px; line-height: 92px; transform: translateX(-50%); }
  .award-date .month { left: 225px; font-size: 25px; letter-spacing: 2px; }
  .award-date .day { left: 352px; font-size: 80px; font-weight: 300; }
  .award-date .year { left: 453px; font-size: 25px; letter-spacing: 1px; }

  .signatures {
    position: absolute; left: 128px; top: 684px;
    width: 394px; height: 214px;
    background: linear-gradient(180deg, var(--sign), #232835);
  }
  .company-name {
    position: absolute; left: 0; top: 906px; width: 100%;
    text-align: center;
    font-size: 30px; line-height: 40px; font-weight: 400;
    color: var(--ink);
  }
</style>
</head>
<body>
  <main class="award-card">
    <div class="frame-line horizontal top-a"></div>
    <div class="frame-line horizontal top-b"></div>
    <div class="frame-line horizontal bottom-a"></div>
    <div class="frame-line horizontal bottom-b"></div>
    <div class="frame-line vertical left-a"></div>
    <div class="frame-line vertical left-b"></div>
    <div class="frame-line vertical right-a"></div>
    <div class="frame-line vertical right-b"></div>

    <div class="corner-ornament top-left" role="img" aria-label="Gold baroque corner ornament"></div>
    <div class="corner-ornament top-right" role="img" aria-label="Gold baroque corner ornament"></div>
    <div class="corner-ornament bottom-left" role="img" aria-label="Gold baroque corner ornament"></div>
    <div class="corner-ornament bottom-right" role="img" aria-label="Gold baroque corner ornament"></div>

    <svg class="heading-arc" viewBox="0 0 685 100">
      <defs>
        <path id="heading-curve" d="M 150 88 Q 342 0 535 88"/>
      </defs>
      <text text-anchor="middle"><textPath href="#heading-curve" startOffset="50%">ANNIVERSARY</textPath></text>
    </svg>
    <div class="years-number">5</div>
    <div class="years-label">YEAR</div>

    <p class="thanks-message">Thank you for being part of our<br>company,s success over these 5<br>years.&nbsp; we greatly appreiate and<br>value your hard worh and<br>commitment to making it work right<br>the first time.</p>

    <div class="gold-rule above-date"></div>
    <div class="award-date">
      <span class="month">NOV</span>
      <span class="day">28</span>
      <span class="year">2019</span>
    </div>
    <div class="gold-rule below-date"></div>

    <div class="signatures" role="img" aria-label="Handwritten team signatures"></div>

    <div class="company-name">KVR Partners</div>
  </main>
</body>
</html>
```